Epoxy Flooring Contractor business card

We need a business card to promote a new addition to our business. We now offer Epoxy Flooring. We would like for the business card to include the images attached. One is our logo, the other is a sample of metallic epoxy flooring, we would like to incorporate that somewhere into the design. I was thinking an icon of a man pushing a concrete grinder and have the color set to the metallic epoxy color. I found a business card sample on this website, I will attach it. It has the icon that we are looking for, or something similar.
Our company name is Harborline Coatings LLC
Our owners name is Dane Morrow
Phone is 561-482-7160
website is www.harborline-coatingsllc.example
please let me know if you need any other info

Contact Information for Business Card

Harborline Coatings LLC
Dane Morrow, owner
Phone: 561-482-7160
Address: P.O Box 8241 Lake Worth, FL 33467
www.Harborline-CoatingsLLC.example
HarborlineCoatingsLLC@mailbox.example
Include logo attached
It must include a Clip art of man with concrete grinder
Must include metallic epoxy design attached
Must include the following text
Residential Garage Flooring
Epoxy Countertops
Commercial Epoxy Flooring
Restaurant Flooring
Warehouse Flooring
Licensed & Insured
Free Estimates

Colors

Designer to choose colors to be used in the design.

Requirements
Must have
• Include logo attached
• It must include a Clip art of man with concrete grinder
• Must include metallic epoxy design attached
• Must include the following text
• Garage Epoxy Flooring
• Residential Epoxy Flooring
• Concrete Floor Crack Repairs
• Concrete Floor Grinding
• Commercial & Warehouse Epoxy Flooring
• Restaurant Epoxy Flooring
• Epoxy Countertops
• Non Slip Epoxy Pool Decks
• Textured Finishes, Flakes, Granite Coat, Metallic & Quartz
• FREE ESTIMATES • LICENSED & INSURED

```html
<!DOCTYPE html>
<html lang="en">
<head>
<meta charset="utf-8">
<title>Harborline Coatings LLC – Business Card</title>
<link rel="stylesheet" href="https://fonts.googleapis.com/css2?family=Arimo:wght@400;700&family=Roboto:ital,wght@0,400;0,500;0,700;1,700;1,900&display=swap">
<style>
  :root{
    --navy:#44648c;
    --navy-deep:#385680;
    --sky:#7ea6d4;
    --royal:#2f5db0;
    --royal-light:#4f7fd0;
    --ink:#555a60;
    --white:#ffffff;
    --backdrop:#e9e7e3;
  }
  *{box-sizing:border-box;margin:0;padding:0}
  html,body{width:1189px;height:1200px;overflow:hidden}
  body{background:var(--backdrop);position:relative;font-family:"Arimo",Arial,sans-serif}

  .card{position:absolute;left:168px;width:853px;overflow:hidden;box-shadow:0 3px 10px rgba(0,0,0,.25)}

  /* Front */
  .card--front{top:111px;height:486px;background:var(--white)}
  .brand{position:absolute;left:36px;top:50px;display:flex;align-items:center;gap:16px}
  .brand__mark{width:64px;height:64px;background:var(--navy)}
  .brand__name{font-size:37px;line-height:1.05;color:var(--ink);letter-spacing:1.5px;font-weight:400}
  .owner{position:absolute;right:39px;top:58px;text-align:right}
  .owner__name{font-size:35px;font-weight:700;line-height:1;color:var(--navy)}
  .owner__name .first{color:var(--sky)}
  .owner__title{font-size:21px;color:var(--ink);margin-top:3px}
  .stripe-light{position:absolute;left:0;right:0;top:183px;height:9px;background:var(--sky)}
  .gallery{position:absolute;left:0;right:0;top:195px;height:218px;background:var(--navy);display:flex;gap:5px;padding:6px 0 6px 0}
  .gallery__photo{flex:1}
  .photo--kitchen{background:linear-gradient(160deg,#b0845a,#6b4a33 60%,#3a2c24)}
  .photo--tub{background:linear-gradient(170deg,#7b7f85 0%,#d9dbdc 45%,#f2f2f0 75%,#bfc1c2)}
  .photo--brush{background:linear-gradient(150deg,#c7b08a 0%,#e6e4e2 40%,#f0eeec 80%)}
  .photo--vanity{background:linear-gradient(170deg,#b9c0c4 0%,#cfbfa0 45%,#ece8e0 80%)}
  .stripe-white{position:absolute;left:0;right:0;top:413px;height:6px;background:var(--white)}
  .contact-bar{position:absolute;left:0;right:0;top:419px;bottom:0;background:var(--navy);display:flex;align-items:center;justify-content:center;gap:10px;color:var(--white);font-size:21px}
  .contact-bar svg{flex:none}
  .contact-bar .sep{margin-right:10px}

  /* Back */
  .card--back{top:640px;height:488px;background:radial-gradient(ellipse at 65% 35%,var(--royal-light),var(--royal) 55%,#244b98);font-family:"Roboto",Arial,sans-serif;color:var(--white)}
  .services__title{position:absolute;left:50px;top:40px;font-size:26px;font-weight:500}
  .services__list{position:absolute;left:50px;top:97px;list-style:none;font-size:20.5px;line-height:30.6px}
  .services__list li{position:relative;padding-left:32px}
  .services__list li::before{content:"";position:absolute;left:2px;top:11px;width:10px;height:10px;border-radius:50%;background:var(--white)}
  .promise{position:absolute;left:479px;top:38px;font-size:28.5px;font-weight:900;font-style:italic;line-height:41px;letter-spacing:.5px}
  .worker{position:absolute;left:530px;top:136px;width:294px;height:352px;background:linear-gradient(180deg,#8fb3e0,#5f86bf 60%,#44648c);border-radius:40px 40px 0 0}
  .back-rule{position:absolute;left:0;right:0;top:426px;height:3px;background:#d7e3f4}
  .web-bar{position:absolute;left:0;right:0;top:429px;bottom:0;background:var(--navy-deep);display:flex;align-items:center;padding-left:50px;font-size:18.5px;font-weight:700;letter-spacing:2px}
</style>
</head>
<body>

<section class="card card--front">
  <div class="brand">
    <div class="brand__mark"></div>
    <div class="brand__name">Harborline<br>Coatings</div>
  </div>
  <div class="owner">
    <div class="owner__name"><span class="first">DANE</span> MORROW</div>
    <div class="owner__title">Owner</div>
  </div>
  <div class="stripe-light"></div>
  <div class="gallery">
    <div class="gallery__photo photo--kitchen" role="img" aria-label="Photo of a refinished kitchen with wood cabinets and dark countertops"></div>
    <div class="gallery__photo photo--tub" role="img" aria-label="Photo of a refinished white clawfoot bathtub against mosaic tile"></div>
    <div class="gallery__photo photo--brush" role="img" aria-label="Photo of a hand applying coating with a brush"></div>
    <div class="gallery__photo photo--vanity" role="img" aria-label="Photo of a bathroom vanity with granite top and white cabinets"></div>
  </div>
  <div class="stripe-white"></div>
  <div class="contact-bar">
    <svg width="22" height="18" viewBox="0 0 22 18" aria-hidden="true"><path d="M1 6c0-3 4-5 10-5s10 2 10 5l-4 1-1-2H6L5 7z" fill="#fff"/><rect x="4" y="8" width="14" height="9" rx="2" fill="#fff"/><circle cx="11" cy="12.5" r="2.5" fill="#44648c"/></svg>
    <span class="sep">561-482-7160 |</span>
    <svg width="24" height="17" viewBox="0 0 24 17" aria-hidden="true"><rect x="1" y="1" width="22" height="15" fill="#fff"/><path d="M1 1l11 9 11-9M1 16l8-7M23 16l-8-7" stroke="#44648c" stroke-width="1.6" fill="none"/></svg>
    <span>HarborlineCoatingsLLC@mailbox.example</span>
  </div>
</section>

<section class="card card--back">
  <h2 class="services__title">SERVICES</h2>
  <ul class="services__list">
    <li>Garage Epoxy Flooring</li>
    <li>Residential Epoxy Flooring</li>
    <li>Concrete Floor Crack Repairs</li>
    <li>Concrete Floor Grinding</li>
    <li>Commercial &amp; Warehouse Epoxy Flooring</li>
    <li>Restaurant Epoxy Flooring</li>
    <li>Epoxy Countertops</li>
    <li>Non Slip Epoxy Pool Decks</li>
    <li>Textured Finishes, Flakes,<br>Granite Coat, Metallic &amp; Quartz</li>
  </ul>
  <p class="promise">FREE ESTIMATES<br>LICENSED &amp; INSURED</p>
  <div class="back-rule"></div>
  <div class="web-bar">www.Harborline-CoatingsLLC.example</div>
  <div class="worker" role="img" aria-label="Clip art of a worker in a cap giving a thumbs up while holding a concrete grinder"></div>
</section>

</body>
</html>
```